quiet meadow therapy (QMT)

I need to build a website for my therapy business.
There are two parts to the website
on the landing page; they choose whether they are therapists making a referral or patients needing more information.
After that, they are taken to their respective pages.
There is the textual information and a referral form on the therapist page, and on the patient page, the text is a bit different, and there will be a booking page on the patient page.
Visually minimal, it's a therapeutic website. I want it clean, clinical, and modern
colors: greenish blue or maybe orangish
PHP/html code
Updates

Hi everyone
I'm very sorry for the lack of responses to your designs. I am trying to work it out, but this platform has been a challenge for me.
I appreciate everyone's efforts, and I am unsure how to rate designs and move forward with the ones I like. There is a 5-star rating, but I don't understand how I'm supposed to politely say that it is not it without feeling like I'm going to affect someone's future rating negatively.
Please understand me. Thank you

Designs look the same

Target Market(s)

therapy and stress management

Industry/Entity Type

stress management therapy

Coding

Coded - Design and coding required

Number of Pages Required

5+ page

Font styles to use
Serif

Colors
0094D4
00A9DD
6FCCEA
C7EBF8
E9F6FB
00AB8E
00BBA5
67D7C9
C6EFE9
E9F9F6

Requirements
Must have
• landing page that that have 2 options. one for therapist another for patient

```html
<!DOCTYPE html>
<html lang="en">
<head>
<meta charset="utf-8">
<title>Quiet Meadow Therapy — Landing &amp; Referral Pages</title>
<link href="https://fonts.googleapis.com/css2?family=Montserrat:wght@400;500;600;700;800&family=Roboto:wght@400;500;700&display=swap" rel="stylesheet">
<style>
:root{
  --board:#898989;
  --white:#ffffff;
  --ink:#1d1d1d;
  --muted:#555b5e;
  --teal:#00a88f;
  --teal-deep:#007a74;
  --teal-bright:#00c98f;
  --orange:#f07b12;
  --orange-soft:#f2a51e;
  --grey-bg:#eeeeee;
}
*{margin:0;padding:0;box-sizing:border-box}
html,body{width:705px;height:1200px;overflow:hidden}
body{background:var(--board);font-family:'Roboto',sans-serif;position:relative;color:var(--ink)}
.abs{position:absolute}
.front{z-index:2}
.heading{font-family:'Montserrat',sans-serif}

/* board labels */
.board-title{position:absolute;font-family:'Montserrat',sans-serif;font-weight:500;font-size:17px;color:var(--white);letter-spacing:.5px}
.spec-title{position:absolute;left:66px;font-family:'Montserrat',sans-serif;font-weight:500;font-size:15px;color:var(--white)}
.spec-line{position:absolute;left:66px;font-family:'Montserrat',sans-serif;font-weight:500;font-size:11px;color:var(--white)}
.swatch{position:absolute;width:13px;height:13px;border-radius:50%}
.swatch.teal{background:linear-gradient(135deg,var(--teal-bright),var(--teal-deep))}
.swatch.orange{background:var(--orange)}

/* shared site parts */
.wordmark{position:absolute;font-family:'Roboto',sans-serif;font-weight:700;color:var(--ink);line-height:1;white-space:nowrap}
.phone{position:absolute;font-family:'Montserrat',sans-serif;font-weight:700;color:var(--teal);display:flex;align-items:center;gap:2px}
.pill{position:absolute;border-radius:10px;font-family:'Montserrat',sans-serif;font-weight:700;color:var(--white);display:flex;align-items:center;justify-content:center;white-space:nowrap}
.pill.orange{background:linear-gradient(90deg,var(--orange-soft),var(--orange))}
.pill.teal{background:linear-gradient(90deg,var(--teal-deep),var(--teal))}
.nav{position:absolute;display:flex;font-family:'Montserrat',sans-serif;font-weight:600;color:var(--ink);white-space:nowrap}
.nav .active{color:var(--teal)}
.photo{position:absolute}

/* landing mockup */
.landing{position:absolute;left:51px;top:93px;width:255px;height:162px;background:var(--white);overflow:hidden;border-top:1px solid var(--teal)}
.landing-footer{position:absolute;left:0;top:146px;width:255px;height:16px;background:linear-gradient(90deg,var(--teal-deep),var(--teal-bright) 55%);color:var(--white);font-size:2.8px;display:flex;align-items:center;justify-content:center}

/* referral page */
.page{position:absolute;left:359px;top:96px;width:255px;height:1007px;background:var(--white);overflow:hidden}
.section-title{position:absolute;font-family:'Montserrat',sans-serif;font-weight:700;font-size:8.5px;color:var(--teal-deep);white-space:nowrap}
.section-title .accent{color:var(--teal)}
.body-copy{position:absolute;font-size:2.6px;line-height:4.6px;color:var(--muted)}
.service-card{position:absolute;width:67px;height:79px;background:var(--white)}
.service-card .thumb{position:absolute;left:0;top:0;width:67px;height:39px}
.service-card h3{position:absolute;top:44px;left:0;width:67px;text-align:center;font-family:'Montserrat',sans-serif;font-weight:500;font-size:3.4px;line-height:4.5px;color:var(--ink)}
.service-card p{position:absolute;top:58px;left:8px;width:51px;text-align:center;font-size:2.3px;line-height:3.9px;color:var(--muted)}
.tick-row{position:absolute;left:30px;width:90px;display:flex;gap:4px;align-items:flex-start}
.tick-row p{font-size:2.6px;line-height:4.7px;color:var(--muted)}
.field{position:absolute;height:7px;background:var(--white);font-size:2.3px;color:var(--muted);padding-left:3px;display:flex;align-items:center}
.footer-col h4{position:absolute;font-family:'Montserrat',sans-serif;font-weight:700;font-size:3.2px;color:var(--ink)}
.footer-link{position:absolute;font-size:2.5px;color:var(--ink)}
.footer-bar{position:absolute;width:1.3px;height:13px;background:var(--teal)}
.social{position:absolute;width:7px;height:7px;border-radius:50%;background:var(--orange)}
</style>
</head>
<body>

<div class="board-title" style="left:76px;top:50px">LANDING PAGE SAMPLE1</div>
<div class="board-title" style="left:418px;top:50px">REFERAL PAGE</div>

<div class="spec-title" style="top:288px">FONTS USED:</div>
<div class="spec-line" style="top:314px">Headings: Montserrat</div>
<div class="spec-line" style="top:331px">Paragrapgh: Roboto</div>

<div class="spec-title" style="top:377px">COLORS</div>
<div class="spec-line" style="top:398px">Greenish blue</div>
<div class="swatch teal" style="left:157px;top:399px"></div>
<div class="spec-line" style="top:421px">Orange</div>
<div class="swatch orange" style="left:121px;top:422px"></div>

<!-- ============ LANDING PAGE ============ -->
<section class="landing">
  <div class="wordmark" style="left:22px;top:9px;font-size:11px">QMT</div>
  <div class="phone" style="left:143px;top:8px;font-size:5px">
    <svg width="4" height="4" viewBox="0 0 24 24"><path fill="#00a88f" d="M6.6 10.8a15 15 0 0 0 6.6 6.6l2.2-2.2c.3-.3.7-.4 1-.2 1.1.4 2.3.6 3.6.6.6 0 1 .4 1 1V20c0 .6-.4 1-1 1A17 17 0 0 1 3 4c0-.6.4-1 1-1h3.5c.6 0 1 .4 1 1 0 1.3.2 2.5.6 3.6.1.3 0 .7-.2 1z"/></svg>
    555 014 2290
  </div>
  <div class="pill orange" style="left:194px;top:6px;width:40px;height:8px;font-size:2.6px">MORE INFORMATION</div>
  <nav class="nav" style="left:79px;top:20px;font-size:2.9px;gap:6.5px">
    <span class="active">HOME</span><span>ABOUT US</span><span>SERVICES</span><span>OUR PRACTITIONERS</span><span>WHAT TO EXPECT</span><span>CONTACT US</span>
  </nav>
  <div class="photo" role="img" aria-label="Photo of a man in a therapy session seated on a sofa, facing a therapist holding a notepad" style="left:0;top:27px;width:175px;height:119px;background:linear-gradient(90deg,#b9b4ad 0%,#8d8c88 35%,#c8c4bf 70%,rgba(255,255,255,0) 100%)"></div>
  <h1 class="heading abs" style="left:141px;top:72px;font-size:9.3px;font-weight:700;color:var(--ink)">WELCOME TO QMT</h1>
  <div class="heading abs" style="left:142px;top:83px;font-size:5.4px;font-weight:700;color:var(--ink)">QUIET MEADOW THERAPY</div>
  <div class="pill orange" style="left:141px;top:99px;width:42px;height:8px;font-size:2.8px">THERAPIST REFERRAL</div>
  <div class="pill teal" style="left:187px;top:99px;width:40px;height:8px;font-size:2.8px">MORE INFORMATION</div>
  <footer class="landing-footer">Copyright © 2022 QMT All rights reserved.</footer>
</section>

<!-- ============ REFERRAL PAGE ============ -->
<main class="page">
  <div class="wordmark" style="left:22px;top:10px;font-size:11px">QMT</div>
  <div class="phone" style="left:142px;top:9px;font-size:5px">
    <svg width="4" height="4" viewBox="0 0 24 24"><path fill="#00a88f" d="M6.6 10.8a15 15 0 0 0 6.6 6.6l2.2-2.2c.3-.3.7-.4 1-.2 1.1.4 2.3.6 3.6.6.6 0 1 .4 1 1V20c0 .6-.4 1-1 1A17 17 0 0 1 3 4c0-.6.4-1 1-1h3.5c.6 0 1 .4 1 1 0 1.3.2 2.5.6 3.6.1.3 0 .7-.2 1z"/></svg>
    555 014 2290
  </div>
  <div class="pill orange" style="left:194px;top:7px;width:40px;height:8px;font-size:2.6px">MORE INFORMATION</div>
  <nav class="nav" style="left:79px;top:21px;font-size:2.9px;gap:6.5px">
    <span class="active">HOME</span><span>ABOUT US</span><span>SERVICES</span><span>OUR PRACTITIONERS</span><span>WHAT TO EXPECT</span><span>CONTACT US</span>
  </nav>

  <!-- hero -->
  <div class="photo" role="img" aria-label="Photo of a counsellor sitting with a distressed young man holding his head in his hands" style="left:0;top:27px;width:255px;height:155px;background:linear-gradient(100deg,#5d6466 0%,#3e4446 40%,#5a5e5c 65%,#7d8584 100%)"></div>
  <div class="heading abs" style="left:0;top:70px;width:255px;text-align:center;font-size:3.7px;font-weight:600;color:var(--white)">QUIET MEADOW THERAPY</div>
  <h1 class="heading abs" style="left:0;top:78px;width:255px;text-align:center;font-size:7px;line-height:8.4px;font-weight:600;color:var(--white)">LOREM IPSUM DOLOR SIT<br>DO EIUSMOD TEMPOR</h1>
  <svg class="abs" style="left:0;top:140px" width="255" height="50" viewBox="0 0 255 50">
    <defs><linearGradient id="swoosh" x1="0" x2="1"><stop offset="0" stop-color="#007a74"/><stop offset="1" stop-color="#00c98f"/></linearGradient></defs>
    <path d="M0,38 C60,10 140,0 255,12 L255,50 L0,50 Z" fill="#ffffff"/>
    <path d="M0,38 C60,10 140,0 255,12 L255,15 C150,6 70,14 0,47 Z" fill="url(#swoosh)"/>
  </svg>

  <!-- services background and curve -->
  <div class="abs" style="left:0;top:300px;width:255px;height:275px;background:var(--grey-bg)"></div>
  <svg class="abs" style="left:0;top:250px" width="255" height="60" viewBox="0 0 255 60">
    <path d="M0,0 L255,0 L255,4 C210,40 150,56 60,56 L0,52 Z" fill="#ffffff"/>
    <path d="M70,56 C150,57 210,42 255,4 L255,12 C210,48 150,59 70,56 Z" fill="url(#swoosh)"/>
  </svg>

  <!-- about -->
  <div class="photo front" role="img" aria-label="Photo of a worried woman in a face mask seated across from a therapist" style="left:21px;top:189px;width:99px;height:82px;border-radius:6px;background:linear-gradient(90deg,#c9c6c1,#e6e4e1 55%,#8a6d5b)"></div>
  <svg class="abs front" style="left:96px;top:252px" width="27" height="27" viewBox="0 0 27 27"><circle cx="13.5" cy="13.5" r="13.5" fill="#00917f"/><path d="M10.5 8.5 L18.5 13.5 L10.5 18.5 Z" fill="#fff"/></svg>
  <h2 class="section-title front" style="left:140px;top:187px"><span>ABOUT </span><span class="accent">US</span></h2>
  <p class="body-copy front" style="left:140px;top:202px;width:95px">Lorem ipsum dolor sit amet, consectetur adipiscing elit, sed do eiusmod tempor incididunt ut labore et dolore magna aliqua. Ut enim ad minim veniam, quis nostrud exercitation ullamco laboris nisi ut aliquip ex ea commodo consequat. Duis aute irure dolor in reprehenderit in voluptate velit esse cillum dolore eu fugiat nulla pariatur. Excepteur sint occaecat cupidatat non proident, sunt in culpa qui officia deserunt mollit anim id est laborum. Sed ut perspiciatis unde omnis iste natus error sit voluptatem accusantium doloremque laudantium, totam rem aperiam, eaque ipsa quae ab illo inventore veritatis.</p>
  <div class="pill orange front" style="left:140px;top:260px;width:28px;height:8px;font-size:2.8px">READ MORE</div>

  <!-- services -->
  <h2 class="section-title" style="left:0;top:331px;width:255px;text-align:center"><span>OUR </span><span class="accent">SERVICES</span></h2>

  <article class="service-card" style="left:21px;top:351px">
    <div class="thumb" role="img" aria-label="Photo of a woman looking out a window" style="background:linear-gradient(90deg,#c8bcb4,#8b6f63)"></div>
    <h3>ANXIETY THERAPY<br>&amp; COUNSELLING</h3>
    <p>Lorem ipsum dolor sit amet, consectetur adipiscing elit, sed do eiusmod tempor inc ididunt ut l magna aliqua.</p>
  </article>
  <article class="service-card" style="left:94px;top:351px">
    <div class="thumb" role="img" aria-label="Photo of a sad woman on a leather sofa" style="background:linear-gradient(90deg,#4a3a46,#9a8c8a)"></div>
    <h3>DEPRESSION<br>COUNSELLING &amp; THERAPY</h3>
    <p>Lorem ipsum dolor sit amet, consectetur adipiscing elit, sed do eiusmod tempor inc ididunt ut l magna aliqua.</p>
  </article>
  <article class="service-card" style="left:166px;top:351px">
    <div class="thumb" role="img" aria-label="Photo of a person curled up on a couch holding their head" style="background:linear-gradient(90deg,#b9aa97,#7d6f5f)"></div>
    <h3>GREIF &amp; LOSS THERAPY<br>&amp; COUNSELLING</h3>
    <p>Lorem ipsum dolor sit amet, consectetur adipiscing elit, sed do eiusmod tempor inc ididunt ut l magna aliqua.</p>
  </article>
  <article class="service-card" style="left:21px;top:436px">
    <div class="thumb" role="img" aria-label="Photo of a counselling session on a blue sofa" style="background:linear-gradient(90deg,#5d4a48,#6f7f9a)"></div>
    <h3>STRESS COUNSELLING<br>&amp; MANAGEMENT</h3>
    <p>Lorem ipsum dolor sit amet, consectetur adipiscing elit, sed do eiusmod tempor inc ididunt ut l magna aliqua.</p>
  </article>
  <article class="service-card" style="left:94px;top:436px">
    <div class="thumb" role="img" aria-label="Photo of a stressed woman at a desk" style="background:linear-gradient(90deg,#d6d3cf,#9b6e5e)"></div>
    <h3>SELF-ESTEEM<br>COUNSELLING &amp; THERAPY</h3>
    <p>Lorem ipsum dolor sit amet, consectetur adipiscing elit, sed do eiusmod tempor inc ididunt ut l magna aliqua.</p>
  </article>
  <article class="service-card" style="left:166px;top:436px">
    <div class="thumb" role="img" aria-label="Photo of a distressed woman speaking with a therapist" style="background:linear-gradient(90deg,#7a6a73,#c9cccf)"></div>
    <h3>PTSD THERAPY &amp;<br>COUNSELLING</h3>
    <p>Lorem ipsum dolor sit amet, consectetur adipiscing elit, sed do eiusmod tempor inc ididunt ut l magna aliqua.</p>
  </article>

  <!-- testimonials -->
  <svg class="abs" style="left:0;top:538px" width="255" height="108" viewBox="0 0 255 108">
    <defs><linearGradient id="sunset" x1="0" y1="0" x2="0" y2="1"><stop offset="0" stop-color="#efa51f"/><stop offset="1" stop-color="#e8731a"/></linearGradient></defs>
    <path d="M0,4 C80,14 170,14 255,4 L255,108 L0,108 Z" fill="url(#sunset)"/>
  </svg>
  <h2 class="heading abs" style="left:0;top:567px;width:255px;text-align:center;font-size:8.3px;font-weight:700;color:var(--white)">CLIENT TESTIMONIALS</h2>
  <svg class="abs" style="left:5px;top:601px" width="10" height="10" viewBox="0 0 10 10"><circle cx="5" cy="5" r="4.4" fill="none" stroke="#fff" stroke-width=".6" opacity=".8"/><path d="M5.8 3 L3.8 5 L5.8 7" fill="none" stroke="#fff" stroke-width=".6"/></svg>
  <svg class="abs" style="left:240px;top:601px" width="10" height="10" viewBox="0 0 10 10"><circle cx="5" cy="5" r="4.4" fill="none" stroke="#fff" stroke-width=".6" opacity=".8"/><path d="M4.2 3 L6.2 5 L4.2 7" fill="none" stroke="#fff" stroke-width=".6"/></svg>
  <div class="photo" role="img" aria-label="Portrait photo of the client giving the testimonial" style="left:49px;top:589px;width:34px;height:34px;border-radius:50%;border:1.2px solid var(--white);background:linear-gradient(180deg,#e9ecef,#6d6f74)"></div>
  <p class="abs" style="left:94px;top:591px;width:112px;font-size:3.7px;line-height:7px;font-style:italic;color:var(--white)">"Lorem ipsum dolor sit amet, consectetur adipiscing elit, sed do eiusmod tempor incididunt ut labore et dolore magna aliqua. ex ea commodo consequat".</p>
  <div class="abs" style="left:94px;top:617px;font-size:3.5px;font-style:italic;color:var(--white)">_ MARA ELLISON</div>

  <!-- why choose us -->
  <h2 class="section-title" style="left:0;top:663px;width:255px;text-align:center"><span>WHY </span><span class="accent">CHOOSE US</span></h2>
  <p class="body-copy" style="left:30px;top:678px;width:195px;text-align:center;line-height:5.8px;font-size:3px">Lorem ipsum dolor sit amet, consectetur adipiscing elit, sed do eiusmod tempor incididunt ut labore et dolore magna aliqua. Ut enim ad minim veniam, quis nostrud exercitation ullamco laboris nisi ut aliquip ex ea commodo consequat. Duis aute irure dolor in reprehenderit in voluptate velit esse cillum dolore eu fugiat nulla pariatur.</p>

  <div class="tick-row" style="top:707px"><svg width="8" height="8" viewBox="0 0 10 10"><path d="M1 5.5 L4 8.5 L9 1.5" fill="none" stroke="#00a88f" stroke-width="1.6"/></svg><p>Lorem ipsum dolor sit amet, consectetur adipiscing elit, sed do eiusmod tempor incididunt ut labore et dolore magna aliqua.</p></div>
  <div class="tick-row" style="top:725px"><svg width="8" height="8" viewBox="0 0 10 10"><path d="M1 5.5 L4 8.5 L9 1.5" fill="none" stroke="#00a88f" stroke-width="1.6"/></svg><p>Lorem ipsum dolor sit amet, consectetur adipiscing elit, sed do eiusmod tempor incididunt ut labore et dolore magna aliqua.</p></div>
  <div class="tick-row" style="top:742px"><svg width="8" height="8" viewBox="0 0 10 10"><path d="M1 5.5 L4 8.5 L9 1.5" fill="none" stroke="#00a88f" stroke-width="1.6"/></svg><p>Lorem ipsum dolor sit amet, consectetur adipiscing elit, sed do eiusmod tempor incididunt ut labore et dolore magna aliqua.</p></div>
  <div class="tick-row" style="top:761px"><svg width="8" height="8" viewBox="0 0 10 10"><path d="M1 5.5 L4 8.5 L9 1.5" fill="none" stroke="#00a88f" stroke-width="1.6"/></svg><p>Lorem ipsum dolor sit amet, consectetur adipiscing elit, sed do eiusmod tempor incididunt ut labore et dolore magna aliqua.</p></div>
  <div class="tick-row" style="top:780px"><svg width="8" height="8" viewBox="0 0 10 10"><path d="M1 5.5 L4 8.5 L9 1.5" fill="none" stroke="#00a88f" stroke-width="1.6"/></svg><p>Lorem ipsum dolor sit amet, consectetur adipiscing elit, sed do eiusmod tempor incididunt ut labore et dolore magna aliqua.</p></div>

  <div class="photo" role="img" aria-label="Photo of an overwhelmed woman covering her face in front of a wall of scribbled thoughts" style="left:137px;top:704px;width:91px;height:89px;border-radius:4px;background:linear-gradient(135deg,#c5c8ca,#8d9296 60%,#3b5c9a)"></div>

  <!-- referral form -->
  <div class="abs" style="left:0;top:822px;width:200px;height:101px;background:linear-gradient(180deg,var(--teal-bright),var(--teal-deep))"></div>
  <div class="abs" style="left:136px;top:820px;width:114px;height:103px;border-radius:0 60px 60px 0;background:linear-gradient(180deg,var(--teal-bright),var(--teal-deep))"></div>
  <div class="photo" role="img" aria-label="Photo of a smiling woman talking with a therapist" style="left:147px;top:831px;width:92px;height:92px;border-radius:50%;background:linear-gradient(90deg,#e7eaec,#b9a79a 55%,#7d6a5f)"></div>
  <h2 class="heading abs" style="left:21px;top:832px;font-size:8.6px;font-weight:700;color:var(--white)">REFERRAL FORM</h2>
  <div class="field" style="left:21px;top:843px;width:52px">Name</div>
  <div class="field" style="left:75px;top:843px;width:53px">Age</div>
  <div class="field" style="left:21px;top:852px;width:52px">Email Address</div>
  <div class="field" style="left:75px;top:852px;width:53px">Phone Number</div>
  <div class="field" style="left:21px;top:862px;width:52px">Gender</div>
  <div class="field" style="left:75px;top:862px;width:53px">DOB</div>
  <div class="field" style="left:21px;top:871px;width:52px">Relationship With Client</div>
  <div class="field" style="left:75px;top:871px;width:53px">Reason For Referral</div>
  <div class="field" style="left:21px;top:881px;width:107px;height:15px;align-items:flex-start;padding-top:2px">Message</div>
  <div class="pill orange" style="left:21px;top:905px;width:26px;height:8px;font-size:2.8px">SUBMIT</div>

  <!-- footer -->
  <div class="wordmark" style="left:29px;top:950px;font-size:11px">QMT</div>
  <div class="social" style="left:25px;top:966px" aria-label="Social link"></div>
  <div class="social" style="left:35px;top:966px" aria-label="Social link"></div>
  <div class="social" style="left:46px;top:966px" aria-label="Social link"></div>
  <div class="social" style="left:56px;top:966px" aria-label="Social link"></div>

  <div class="footer-bar" style="left:77px;top:941px"></div>
  <div class="footer-bar" style="left:126px;top:941px"></div>
  <div class="footer-bar" style="left:182px;top:941px"></div>

  <div class="footer-col">
    <h4 style="left:89px;top:944px">NAVIGATION</h4>
    <div class="footer-link" style="left:89px;top:952px">Home</div>
    <div class="footer-link" style="left:89px;top:959px">About Us</div>
    <div class="footer-link" style="left:89px;top:966px">Our Practitioners</div>
    <div class="footer-link" style="left:89px;top:972px">What To Expect</div>
    <div class="footer-link" style="left:89px;top:979px">Contact Us</div>
  </div>
  <div class="footer-col">
    <h4 style="left:138px;top:944px">AWARENESS</h4>
    <div class="footer-link" style="left:138px;top:952px">Choosing a therapist</div>
    <div class="footer-link" style="left:138px;top:959px">Find a therapist</div>
    <div class="footer-link" style="left:138px;top:966px">Types of therapists</div>
    <div class="footer-link" style="left:138px;top:972px">Types of therapies</div>
    <div class="footer-link" style="left:138px;top:979px">Helpfull resources</div>
  </div>
  <div class="footer-col">
    <h4 style="left:196px;top:944px">CONTACT US</h4>
    <svg class="abs" style="left:196px;top:952px" width="6" height="6" viewBox="0 0 12 12"><circle cx="6" cy="6" r="6" fill="#f07b12"/><path d="M6 2.6a2.3 2.3 0 0 0-2.3 2.3C3.7 6.6 6 9.4 6 9.4s2.3-2.8 2.3-4.5A2.3 2.3 0 0 0 6 2.6z" fill="#fff"/></svg>
    <div class="footer-link" style="left:205px;top:951px;width:30px;line-height:4.6px">123 Lorem Way, consectetur adipiscing elit,</div>
    <svg class="abs" style="left:196px;top:968px" width="6" height="6" viewBox="0 0 12 12"><circle cx="6" cy="6" r="6" fill="#f07b12"/><path d="M4 3.3l1.2 1.6-.6.8a4.6 4.6 0 0 0 1.8 1.8l.8-.6 1.6 1.2-.6 1c-2.7-.2-4.9-2.4-5.1-5.1z" fill="#fff"/></svg>
    <div class="footer-link" style="left:206px;top:969px">555 014 2290</div>
    <svg class="abs" style="left:196px;top:977px" width="6" height="6" viewBox="0 0 12 12"><circle cx="6" cy="6" r="6" fill="#f07b12"/><rect x="3" y="4" width="6" height="4.2" fill="#fff"/><path d="M3 4 L6 6.4 L9 4" fill="none" stroke="#f07b12" stroke-width=".6"/></svg>
    <div class="footer-link" style="left:206px;top:978px">hello@qmt-care.com</div>
  </div>

  <div class="abs" style="left:0;top:992px;width:255px;height:.5px;background:#e3e3e3"></div>
  <div class="abs" style="left:0;top:997px;width:255px;text-align:center;font-size:2.6px;color:var(--ink)">Copyright © 2022 QMT All rights reserved.</div>
</main>

</body>
</html>
```